Heron Hollow Post Card

I am a real estate agent with Wexford and Partners. I would like to have two post cards designed. A Just Listed and a Just Sold post card for the bay front community of Heron Hollow. Heron Hollow is a residential community located on the Gulf coast of Florida. It is bordered by Pelican Sound on one side of the road and Coral Dune Golf Course on the other side of the road. I am uploading several images that can be used on the design of the postcard as well as an example of what I would like to be included on the back. They will be oversized postcards and color on both sides.

Industry/Entity Type

Real Estate

```html
<!DOCTYPE html>
<html lang="en">
<head>
<meta charset="utf-8">
<title>Heron Hollow – Just Listed Postcard</title>
<link rel="stylesheet" href="https://fonts.googleapis.com/css2?family=Cinzel:wght@400;700&family=Italianno&display=swap">
<style>
  :root {
    --ink: #111111;
    --band: #0b0b0b;
    --paper: #ffffff;
    --sky-panel: #aab8d8;
    --white: #ffffff;
    --rule: #222222;
    --badge: #2b2b2b;
  }
  * { margin: 0; padding: 0; box-sizing: border-box; }
  html, body { width: 870px; height: 1200px; overflow: hidden; background: var(--paper); }
  .postcard { position: relative; width: 870px; height: 1200px; font-family: "Cinzel", serif; color: var(--ink); }

  /* Front */
  .front { position: absolute; left: 0; top: 0; width: 870px; height: 575px; }
  .front-art { position: absolute; left: 0; top: 0; }
  .community-title {
    position: absolute; left: 22px; top: 22px;
    font-weight: 700; font-size: 35px; line-height: 44px; color: var(--ink);
  }
  .brand-mark {
    position: absolute; left: 20px; top: 195px; width: 170px;
    display: flex; align-items: center; gap: 8px;
    font-size: 14px; font-weight: 700; line-height: 17px; color: var(--ink);
  }
  .brand-mark .square { width: 22px; height: 22px; background: var(--ink); flex: none; }
  .community-blurb {
    position: absolute; left: 20px; top: 335px; width: 185px;
    font-size: 15px; line-height: 19px; color: var(--white); text-transform: uppercase;
  }

  /* Back */
  .divider { position: absolute; left: 0; top: 637px; width: 870px; height: 1px; background: var(--rule); }
  .back-brand {
    position: absolute; left: 25px; top: 680px; width: 170px;
    display: flex; align-items: center; gap: 8px;
    font-size: 14px; font-weight: 700; line-height: 17px; color: var(--ink);
  }
  .back-brand .square { width: 22px; height: 22px; background: var(--ink); flex: none; }
  .agent-address {
    position: absolute; left: 205px; top: 663px;
    font-size: 19px; line-height: 24px; color: var(--ink);
  }
  .community-badge { position: absolute; left: 493px; top: 712px; }
  .headline {
    position: absolute; left: 98px; top: 768px;
    font-family: "Italianno", cursive; font-size: 104px; line-height: 1; color: var(--ink);
  }
  .address-line { position: absolute; left: 50px; top: 912px; width: 463px; height: 1.5px; background: var(--rule); }
  .listing-location {
    position: absolute; left: 50px; top: 926px; width: 463px; text-align: center;
    font-size: 27px; color: var(--ink);
  }
  .listing-terms {
    position: absolute; left: 44px; top: 978px;
    font-size: 15px; color: var(--ink); display: flex; align-items: flex-end; gap: 6px;
  }
  .blank { display: inline-block; border-bottom: 1px solid var(--rule); height: 16px; }
  .blank.price { width: 186px; margin-right: 22px; }
  .blank.date { width: 196px; }
  .invitation {
    position: absolute; left: 60px; top: 1036px; width: 440px; text-align: center;
    font-size: 15px; line-height: 19px; color: var(--ink);
  }
  .agent-phone { position: absolute; left: 72px; top: 1088px; font-size: 36px; color: var(--ink); }
  .agent-email { position: absolute; left: 52px; top: 1137px; font-size: 15px; color: var(--ink); text-transform: lowercase; }
</style>
</head>
<body>
<main class="postcard">

  <section class="front">
    <svg class="front-art" width="870" height="575" viewBox="0 0 870 575">
      <defs>
        <linearGradient id="estateGrad" x1="0" y1="0" x2="0" y2="1">
          <stop offset="0" stop-color="#8fb0d8"/>
          <stop offset="0.45" stop-color="#dfe6ea"/>
          <stop offset="0.7" stop-color="#7d9268"/>
          <stop offset="1" stop-color="#6f9a4c"/>
        </linearGradient>
        <linearGradient id="dockGrad" x1="0" y1="0" x2="0" y2="1">
          <stop offset="0" stop-color="#4a8fd3"/>
          <stop offset="0.45" stop-color="#9cc2e6"/>
          <stop offset="0.55" stop-color="#2f6e98"/>
          <stop offset="1" stop-color="#5b4e3c"/>
        </linearGradient>
        <linearGradient id="gateGrad" x1="0" y1="0" x2="0" y2="1">
          <stop offset="0" stop-color="#3f86d0"/>
          <stop offset="0.5" stop-color="#8fb7dc"/>
          <stop offset="0.75" stop-color="#4f7a3c"/>
          <stop offset="1" stop-color="#b9b2a2"/>
        </linearGradient>
      </defs>
      <rect class="title-panel" x="0" y="0" width="270" height="292" fill="var(--sky-panel)"/>
      <rect class="info-band" x="0" y="288" width="870" height="287" fill="var(--band)"/>
      <path role="img" aria-label="Photo of waterfront homes with palms across a pond"
            d="M265 0 Q218 120 208 292 L870 292 L870 0 Z" fill="url(#estateGrad)"/>
      <rect role="img" aria-label="Photo of a wooden dock reaching into the sound"
            x="207" y="300" width="311" height="268" fill="url(#dockGrad)"/>
      <path role="img" aria-label="Photo of the community entrance gate with flag and palms"
            d="M528 300 L836 300 Q858 434 836 568 L528 568 Z" fill="url(#gateGrad)"/>
    </svg>

    <h1 class="community-title">Heron<br>Hollow</h1>
    <div class="brand-mark"><span class="square"></span><span>Wexford and Partners</span></div>
    <p class="community-blurb">A one of kind, upscale gated community located on Cape Haze Peninsula and nestled between the Coral Dune Golf Course and Pelican Sound.</p>
  </section>

  <div class="divider"></div>

  <section class="back">
    <div class="back-brand"><span class="square"></span><span>Wexford and Partners</span></div>
    <address class="agent-address" style="font-style: normal;">
      Marina Calloway<br>
      2740 Tidewater Cove Dr<br>
      Unit B14<br>
      Seabright, FL&nbsp; 34029
    </address>

    <svg class="community-badge" width="200" height="128" viewBox="0 0 200 128" role="img" aria-label="Community plaque">
      <ellipse cx="100" cy="72" rx="96" ry="46" fill="var(--badge)"/>
      <ellipse cx="100" cy="72" rx="86" ry="38" fill="none" stroke="#bdbdbd" stroke-width="2"/>
    </svg>

    <h2 class="headline">Just Listed</h2>
    <div class="address-line"></div>
    <p class="listing-location">In HERON HOLLOW</p>
    <p class="listing-terms">at $<span class="blank price"></span>On <span class="blank date"></span></p>
    <p class="invitation">Please contact me if you are interested<br>in buying or selling property in the area.</p>
    <p class="agent-phone">555-318-4720</p>
    <p class="agent-email">marina.calloway@example.com</p>
  </section>

</main>
</body>
</html>
```